Letterhead Design Project for online gaming site

We need a letterhead for a new online gaming company. The site is www.lunaroller.co

The logo is a gold colour and the site is similar in nature. Feel free to take a look at the landing page.

However the designer has free reign to do whatever they like with it.

OTHER CONTENT:

Telephone: 1300 746 315
Email: info@lunaroller.co
Web: www.lunaroller.co

Industry/Entity Type

It Company

```html
<!DOCTYPE html>
<html lang="en">
<head>
<meta charset="utf-8">
<title>LunaRoller.co Letterhead</title>
<link rel="stylesheet" href="https://fonts.googleapis.com/css2?family=Ubuntu:wght@700&family=Open+Sans:wght@400;600&display=swap">
<style>
  :root {
    --ink-black: #050505;
    --paper: #ffffff;
    --paper-shade: #f3f3f3;
    --gold-light: #f7dc1e;
    --gold-deep: #b08a1a;
    --gold-text: #e9c21c;
    --band-dark: #2a2a2a;
    --band-mid: #6a6a6a;
    --footer-text: #3a2f10;
    --web-text: #ffffff;
    --silhouette: #c9c9c9;
  }
  * { margin: 0; padding: 0; box-sizing: border-box; }
  html, body {
    width: 967px;
    height: 1200px;
    overflow: hidden;
    background: var(--paper);
  }
  .letterhead {
    position: relative;
    width: 967px;
    height: 1200px;
    background: linear-gradient(175deg, var(--paper) 0%, var(--paper-shade) 45%, var(--paper) 100%);
    font-family: "Open Sans", Arial, sans-serif;
  }
  .masthead {
    position: absolute;
    top: 0; left: 0;
    width: 100%;
    height: 130px;
    background: var(--ink-black);
    display: flex;
    align-items: center;
    justify-content: center;
  }
  .brand-name {
    font-family: "Ubuntu", Arial, sans-serif;
    font-weight: 700;
    font-size: 64px;
    letter-spacing: -1px;
    color: var(--gold-text);
    line-height: 1;
  }
  .racing-scene {
    position: absolute;
    left: 78px;
    top: 900px;
    width: 820px;
    height: 232px;
    background: radial-gradient(ellipse at 45% 60%, rgba(201,201,201,0.55) 0%, rgba(201,201,201,0.25) 50%, rgba(255,255,255,0) 75%);
  }
  .footer-band {
    position: absolute;
    left: 0;
    top: 1136px;
    width: 967px;
    height: 40px;
  }
  .footer-band svg { position: absolute; left: 0; top: 0; }
  .contact-list {
    position: absolute;
    left: 44px;
    top: 0;
    height: 40px;
    display: flex;
    align-items: center;
    gap: 22px;
    font-size: 14px;
    color: var(--footer-text);
  }
  .contact-item { display: flex; align-items: center; gap: 5px; }
  .contact-item svg { position: static; }
  .web-address {
    position: absolute;
    right: 40px;
    top: 0;
    height: 40px;
    display: flex;
    align-items: center;
    font-size: 15px;
    letter-spacing: 3px;
    color: var(--web-text);
  }
</style>
</head>
<body>
<div class="letterhead">
  <header class="masthead">
    <span class="brand-name">LunaRoller.co</span>
  </header>

  <div class="racing-scene" role="img" aria-label="Faint grey silhouettes of harness racing, a galloping racehorse with jockey, and greyhounds running"></div>

  <footer class="footer-band">
    <svg width="967" height="40" viewBox="0 0 967 40" aria-hidden="true">
      <defs>
        <linearGradient id="goldBand" x1="0" x2="1" y1="0" y2="0">
          <stop offset="0" stop-color="var(--gold-deep)"/>
          <stop offset="0.55" stop-color="#d8b21c"/>
          <stop offset="1" stop-color="var(--gold-light)"/>
        </linearGradient>
        <linearGradient id="darkBand" x1="0" x2="1" y1="0" y2="0">
          <stop offset="0" stop-color="var(--band-mid)"/>
          <stop offset="0.3" stop-color="var(--band-dark)"/>
          <stop offset="1" stop-color="var(--ink-black)"/>
        </linearGradient>
      </defs>
      <polygon points="0,0 648,0 612,40 0,40" fill="url(#goldBand)"/>
      <polygon points="672,0 967,0 967,40 636,40" fill="url(#darkBand)"/>
    </svg>
    <div class="contact-list">
      <span class="contact-item">
        <svg width="14" height="14" viewBox="0 0 14 14" aria-hidden="true"><circle cx="7" cy="7" r="6" fill="none" stroke="currentColor" stroke-width="1.2"/><path d="M5 4.2c-.6 2 .8 4.6 3.6 5.6l.8-1-1.2-.8-.6.5C6.9 8 6.2 7 6 6l.6-.4-.4-1.4z" fill="currentColor"/></svg>
        1300 746 315
      </span>
      <span class="contact-item">
        <svg width="15" height="12" viewBox="0 0 15 12" aria-hidden="true"><rect x="1" y="1" width="13" height="10" rx="1" fill="none" stroke="currentColor" stroke-width="1.2"/><path d="M1.5 1.8 7.5 6.5l6-4.7" fill="none" stroke="currentColor" stroke-width="1.2"/></svg>
        info@lunaroller.co
      </span>
    </div>
    <div class="web-address">www.lunaroller.co</div>
  </footer>
</div>
</body>
</html>
```